Fitness & sports performance company needs a landing page design

Looking for a landing page for a fitness & sports performance company based in South Florida. The company is 'The Larkfield Fitness Studio', and 'The Larkfield' for short. The main objective of the landing page is to generate leads, and show potential clients the services we offer, as well as pricing for each service. While we are based in South Florida, we also offer online services such as an online trainer and online strength & conditioning programs. Would like to see designs that utilize the colors in our logo.

Target Market(s)

those looking to lose weight, gain strength and make overall healthy lifestyle changes

Font styles to use
Sans Serif

Colors
60b9df
57b5de

Requirements
Must have
• a place to list testimonials, list of services provided, show pricing for each service, colors of the website matching colors in the logo
Nice to have
• i would like to see a landing page that can be utilized to create leads and an email list

```html
<!DOCTYPE html>
<html lang="en">
<head>
<meta charset="utf-8">
<title>The Larkfield Fitness Studio</title>
<link href="https://fonts.googleapis.com/css2?family=Arimo:wght@400;700&display=swap" rel="stylesheet">
<style>
:root{
  --teal:#3bc1d1;
  --teal-soft:#cbeef2;
  --teal-pale:#e9f6f8;
  --teal-light:#7fd6e0;
  --ink:#2b2b2b;
  --ink-field:#333333;
  --white:#ffffff;
  --text:#222222;
  --muted:#9a9a9a;
}
*{margin:0;padding:0;box-sizing:border-box}
html,body{width:1200px;height:2927px;overflow:hidden}
body{position:relative;font-family:"Arimo",Arial,sans-serif;background:var(--white);color:var(--text)}
.abs{position:absolute}

/* header */
.site-header{left:0;top:0;width:1200px;height:98px;background:var(--teal)}
.brand{left:30px;top:30px;display:flex;align-items:center;gap:10px;color:var(--white);font-weight:700;font-size:17px}
.brand-dot{width:34px;height:34px;border-radius:50%;background:var(--white)}
.main-nav{top:42px;font-size:11px;font-weight:700;color:var(--white);letter-spacing:.3px}
.signup-btn{left:1083px;top:31px;width:84px;height:35px;background:var(--teal-pale);color:var(--ink);font-size:10px;font-weight:700;display:flex;align-items:center;justify-content:center}

/* hero */
.hero-backdrop{left:0;top:98px;width:1200px;height:546px;background:var(--white)}
.teal-band{left:0;top:644px;width:1200px;height:917px;background:var(--teal)}
.hero{left:16px;top:98px;width:1164px;height:634px;background:linear-gradient(120deg,#4a4a4a 0%,#8d8d8d 35%,#b9b2a8 60%,#5e5e5e 100%);box-shadow:0 12px 24px rgba(0,0,0,.35)}
.form-title{left:51px;top:156px;width:314px;height:68px;background:var(--ink);color:var(--white);font-size:28px;font-weight:700;display:flex;align-items:center;justify-content:center}
.field{left:51px;width:314px;height:47px;background:var(--ink-field);color:var(--white);font-size:13px;display:flex;align-items:center;padding-left:18px}
.field.placeholder{color:var(--muted)}
.enter-btn{left:51px;top:556px;width:314px;height:76px;background:var(--teal);color:var(--white);font-size:36px;font-weight:700;display:flex;align-items:center;justify-content:center}
.social{top:685px;width:16px;height:16px;border-radius:50%;background:rgba(255,255,255,.85)}
.hero-title{right:117px;top:528px;font-size:52px;font-weight:700;color:var(--teal);letter-spacing:-.5px}
.hero-text{right:117px;top:596px;width:440px;text-align:right;font-size:17px;line-height:27px;color:var(--white)}
.dots{left:580px;top:510px;display:flex;gap:8px}
.dots span{width:6px;height:6px;border-radius:50%;background:var(--teal)}

/* services */
.services-title{left:0;top:806px;width:1200px;text-align:center;font-size:37px;color:var(--white)}
.services-sub{left:0;top:853px;width:1200px;text-align:center;font-size:12px;font-weight:700;color:var(--white)}
.price-card{top:923px;width:296px;height:535px;background:var(--white)}
.card-label{left:27px;top:27px;font-size:9px;font-weight:700;color:var(--teal)}
.plus{right:27px;top:25px;width:34px;height:34px;border-radius:50%;background:var(--teal-pale);color:var(--teal);font-size:26px;display:flex;align-items:center;justify-content:center;line-height:1}
.price{left:0;top:117px;width:100%;text-align:center;font-size:36px;font-weight:700;color:var(--teal)}
.price sup{font-size:13px;vertical-align:18px;margin-right:6px}
.features{left:0;top:204px;width:100%;text-align:center;font-size:13px;font-weight:700;color:var(--teal);line-height:27px}
.chart{left:78px;top:335px}
.includes{left:767px;top:923px;width:298px;height:535px;border:1.5px solid rgba(255,255,255,.7);color:var(--white)}
.includes .card-label{color:var(--white)}
.kebab{right:24px;top:22px;font-size:16px;font-weight:700}
.include-list{left:78px;top:76px;list-style:none;font-size:11px;font-weight:700}
.include-list li{height:44px;display:flex;align-items:flex-start;gap:18px}
.divider{left:27px;top:315px;width:244px;height:1.5px;background:rgba(255,255,255,.85)}
.testimonial-avatar{left:27px;top:354px;width:34px;height:34px;border-radius:50%;background:var(--white);display:flex;align-items:center;justify-content:center}
.testimonial-name{left:80px;top:358px;font-size:12px;font-weight:700}
.testimonial-role{left:80px;top:374px;font-size:8px}
.testimonial-quote{left:80px;top:410px;width:180px;font-size:11px;font-weight:700;line-height:21px}

/* team */
.member-photo{top:1684px;width:281px;height:140px;background:#333333;display:flex;align-items:center;justify-content:center}
.member-name{top:1860px;font-size:18px;font-weight:700;color:var(--teal)}
.member-role{top:1886px;font-size:8px;font-weight:700;color:var(--teal)}
.member-bio{top:1903px;width:281px;font-size:11px;line-height:21px;color:var(--text)}
.scroll-down{left:576px;top:2088px;width:62px;height:62px;border-radius:50%;background:var(--teal);display:flex;align-items:center;justify-content:center}

/* newsletter */
.newsletter{left:0;top:2253px;width:1200px;height:615px;background:var(--teal-pale)}
.newsletter-title{left:396px;top:2485px;width:520px;font-size:35px;line-height:45px;color:var(--teal)}
.newsletter-input{left:396px;top:2599px;width:349px;height:33px;background:var(--white);border:1.5px solid var(--teal-soft);color:#b8b8b8;font-size:10px;display:flex;align-items:center;padding-left:14px}
.send-btn{left:765px;top:2599px;width:103px;height:33px;background:var(--teal);color:var(--white);font-size:9px;font-weight:700;display:flex;align-items:center;justify-content:center}

/* footer */
.site-footer{left:0;top:2868px;width:1200px;height:59px;background:var(--teal)}
.footer-brand{left:28px;top:2880px;display:flex;align-items:center;gap:8px;color:var(--white);font-weight:700;font-size:13px}
.footer-brand span.dot{width:26px;height:26px;border-radius:50%;background:var(--white)}
.footer-nav{top:2892px;font-size:10px;font-weight:700;color:var(--white)}
.back-to-top{left:1095px;top:2868px;width:105px;height:59px;background:var(--teal-light);display:flex;align-items:center;justify-content:center}
</style>
</head>
<body>

<header class="abs site-header"></header>
<div class="abs brand"><span class="brand-dot"></span>The Larkfield</div>
<nav>
  <span class="abs main-nav" style="left:692px">FEED</span>
  <span class="abs main-nav" style="left:756px">AUTHORS</span>
  <span class="abs main-nav" style="left:838px">EXPLORE</span>
  <span class="abs main-nav" style="left:920px">BLOG</span>
  <span class="abs main-nav" style="left:984px">CONTACT</span>
</nav>
<div class="abs signup-btn">SIGN UP</div>

<div class="abs hero-backdrop"></div>
<div class="abs teal-band"></div>
<section class="abs hero" role="img" aria-label="Athlete doing push-ups on a gym floor"></section>

<div class="abs form-title">SIGN UP NOW</div>
<div class="abs field placeholder" style="top:248px">Required Field</div>
<div class="abs field placeholder" style="top:309px">Focused</div>
<div class="abs field" style="top:371px">Typing|</div>
<div class="abs field" style="top:433px">Entered</div>
<div class="abs field" style="top:494px">name@mailbox.test
  <svg style="position:absolute;right:14px;top:16px" width="15" height="15" viewBox="0 0 15 15"><circle cx="7.5" cy="7.5" r="7" fill="#fff"/><rect x="6.6" y="3.5" width="1.8" height="5" fill="#333"/><rect x="6.6" y="9.8" width="1.8" height="1.8" fill="#333"/></svg>
</div>
<div class="abs enter-btn">Enter</div>
<span class="abs social" style="left:49px"></span>
<span class="abs social" style="left:88px"></span>
<span class="abs social" style="left:125px"></span>
<span class="abs social" style="left:166px"></span>

<div class="abs dots"><span></span><span></span><span></span><span></span></div>
<h1 class="abs hero-title">THE LARKFIELD</h1>
<p class="abs hero-text">Excepteur sint occaecat cupidatat non proident, sunt in culpa qui officia deserunt</p>

<h2 class="abs services-title">Our Services</h2>
<p class="abs services-sub">Excepteur sint occaecat cupidatat non proident, sunt in culpa qui officia deserunt</p>

<article class="abs price-card" style="left:135px">
  <span class="abs card-label">STANDART</span>
  <span class="abs plus">+</span>
  <div class="abs price"><sup>$</sup>39.99</div>
  <div class="abs features">5 USERS<br>5000 MOCKUPS<br>SKETCHWELL APP</div>
  <svg class="abs chart" width="140" height="140" viewBox="0 0 140 140">
    <circle cx="70" cy="70" r="70" fill="#cbeef2"/>
    <path d="M70 70 L70 0 A70 70 0 0 1 118 121 Z" fill="#3bc1d1"/>
  </svg>
</article>

<article class="abs price-card" style="left:451px">
  <span class="abs card-label">UNLIMITED</span>
  <span class="abs plus">+</span>
  <div class="abs price"><sup>$</sup>79.99</div>
  <div class="abs features">5 USERS<br>5000 MOCKUPS<br>SKETCHWELL APP<br>UNLIMITED UPDATE</div>
  <svg class="abs chart" width="160" height="140" viewBox="0 0 160 140" style="left:68px">
    <polygon points="40,0 120,0 160,70 120,140 40,140 0,70" fill="#cbeef2"/>
    <polygon points="120,0 160,70 80,70" fill="#3bc1d1"/>
    <polygon points="0,70 80,70 40,140" fill="#3bc1d1"/>
    <polygon points="80,70 160,70 120,140" fill="#8fdce5"/>
  </svg>
</article>

<aside class="abs includes">
  <span class="abs card-label">EACH PACK INCLUDES</span>
  <span class="abs kebab">&#8942;</span>
  <ul class="abs include-list">
    <li><svg width="14" height="10" viewBox="0 0 14 10"><path d="M1 5 L5 9 L13 1" stroke="#fff" stroke-width="1.6" fill="none"/></svg>Lorem ipsum</li>
    <li><svg width="14" height="10" viewBox="0 0 14 10"><path d="M1 5 L5 9 L13 1" stroke="#fff" stroke-width="1.6" fill="none"/></svg>Dolor sit amet</li>
    <li><svg width="14" height="10" viewBox="0 0 14 10"><path d="M1 5 L5 9 L13 1" stroke="#fff" stroke-width="1.6" fill="none"/></svg>Consectetur adipisicin</li>
    <li><svg width="14" height="10" viewBox="0 0 14 10"><path d="M1 5 L5 9 L13 1" stroke="#fff" stroke-width="1.6" fill="none"/></svg>Sed do eiusmo</li>
    <li><svg width="14" height="10" viewBox="0 0 14 10"><path d="M1 5 L5 9 L13 1" stroke="#fff" stroke-width="1.6" fill="none"/></svg>Tempor incididunt</li>
  </ul>
  <div class="abs divider"></div>
  <div class="abs testimonial-avatar"><svg width="16" height="16" viewBox="0 0 16 16"><circle cx="8" cy="5" r="3.4" fill="#3bc1d1"/><path d="M1.5 15 C2 10 14 10 14.5 15 Z" fill="#3bc1d1"/></svg></div>
  <span class="abs testimonial-name">Name Surname</span>
  <span class="abs testimonial-role">Founder &amp; CEO Sketchwell</span>
  <p class="abs testimonial-quote">Natus error sit voluptatem accusantium doloremque laudantium, totam rem aperiam, eaque ipsa quae ab illo</p>
</aside>

<section>
  <div class="abs member-photo" style="left:135px"><svg width="72" height="72" viewBox="0 0 72 72"><circle cx="36" cy="22" r="16" fill="#fff"/><path d="M2 72 C4 44 68 44 70 72 Z" fill="#fff"/></svg></div>
  <div class="abs member-photo" style="left:468px"><svg width="72" height="72" viewBox="0 0 72 72"><circle cx="36" cy="22" r="16" fill="#fff"/><path d="M2 72 C4 44 68 44 70 72 Z" fill="#fff"/></svg></div>
  <div class="abs member-photo" style="left:802px"><svg width="72" height="72" viewBox="0 0 72 72"><circle cx="36" cy="22" r="16" fill="#fff"/><path d="M2 72 C4 44 68 44 70 72 Z" fill="#fff"/></svg></div>

  <h3 class="abs member-name" style="left:135px">Name Surname</h3>
  <span class="abs member-role" style="left:135px">CO-FOUNDER &amp; CTO</span>
  <p class="abs member-bio" style="left:135px">Lorem ipsum dolor sit amet, consectetur adipisicing elit, sed do eiusmod tempor incididunt ut ero labore et dolore.</p>

  <h3 class="abs member-name" style="left:468px">Name Surname</h3>
  <span class="abs member-role" style="left:468px">CO-FOUNDER &amp; CTO</span>
  <p class="abs member-bio" style="left:468px">Lorem ipsum dolor sit amet, consectetur adipisicing elit, sed do eiusmod tempor incididunt ut ero labore et dolore.</p>

  <h3 class="abs member-name" style="left:802px">Name Surname</h3>
  <span class="abs member-role" style="left:802px">CO-FOUNDER &amp; CTO</span>
  <p class="abs member-bio" style="left:802px">Lorem ipsum dolor sit amet, consectetur adipisicing elit, sed do eiusmod tempor incididunt ut ero labore et dolore.</p>
</section>

<div class="abs scroll-down"><svg width="18" height="18" viewBox="0 0 18 18"><path d="M9 2 V15 M4 10 L9 15 L14 10" stroke="#fff" stroke-width="2" fill="none"/></svg></div>

<section class="abs newsletter"></section>
<h2 class="abs newsletter-title">Excepteur sint occaecat cupidatat non proident, sunt in</h2>
<div class="abs newsletter-input">Required Field</div>
<div class="abs send-btn">SEND</div>

<footer class="abs site-footer"></footer>
<div class="abs footer-brand"><span class="dot"></span>The Larkfield</div>
<span class="abs footer-nav" style="left:502px">NEWS</span>
<span class="abs footer-nav" style="left:566px">SPORT</span>
<span class="abs footer-nav" style="left:638px">VACATION</span>
<span class="abs footer-nav" style="left:726px">FUTURE</span>
<div class="abs back-to-top"><svg width="18" height="18" viewBox="0 0 18 18"><path d="M9 16 V3 M4 8 L9 3 L14 8" stroke="#fff" stroke-width="2" fill="none"/></svg></div>

</body>
</html>
```